Brightmoor Fire Solutions business card, logo and web design.

We need business cards for our new company. We are based in South Africa. We specialise in fire detection, fire prevention, security, access control and CCTV in buildings. We service and install sprinkler systems, fire hose reals and fire extinguishers in buildings. Our slogan in the company is "Compliance is our business" . We strive to be innovators in our field and deliver the best service possible at the best quality. We want to be the best in our field. We don't have any colour preferences as long as it relates to our type of business.
Our target market is clients that owns big buildings with multiple levels, such a malls,office buildings or warehouses.

Target Market(s)

Industry/Entity Type

Fire Safety

Contact Information for Business Card

The front of the card should have the company name (Brightmoor Fire Solutions (PTY) LTD. and a description of the company. Fire engineering & security services.

Logo Text

Compliance is our business

Number of Pages Required

4 page

Font styles to use
Serif

Colors

Designer to choose colors to be used in the design.

Requirements
Must have
• The company name, the logo and all the details on the back of the card. It should be simple and not to busy.
Nice to have
• Just something different and new. Brightmoor means - innovate so the card should represent our name.
Should not have
• Small pictures or lots of graphics on.

```html
<!DOCTYPE html>
<html lang="en">
<head>
<meta charset="utf-8">
<title>Brightmoor Fire Solutions – Business Card</title>
<link href="https://fonts.googleapis.com/css2?family=Montserrat:wght@400;500;700&display=swap" rel="stylesheet">
<style>
  :root {
    --backdrop: #bcbcbc;
    --card-light: #ebe9e6;
    --card-dark: #1f1f1f;
    --ink-dark: #3a3a3a;
    --ink-mid: #7a7a7a;
    --ink-light: #f2f2f2;
    --ink-soft: #cfcfcf;
  }
  * { margin: 0; padding: 0; box-sizing: border-box; }
  html, body {
    width: 1200px; height: 900px; overflow: hidden;
    background: var(--backdrop);
    font-family: "Montserrat", sans-serif;
  }
  .canvas { position: relative; width: 1200px; height: 900px; }

  .card { position: absolute; }

  /* Front */
  .card-front {
    left: 146px; top: 417px; width: 544px; height: 305px;
    background: var(--card-light);
    text-align: center;
  }
  .company-name {
    position: absolute; left: 0; right: 0; top: 128px;
    color: var(--ink-dark);
    font-size: 27px; font-weight: 700; line-height: 1;
    letter-spacing: 0.5px;
  }
  .front-rule {
    position: absolute; left: 152px; top: 247px; width: 238px; height: 2px;
    background: var(--ink-mid); opacity: 0.7;
  }
  .company-description {
    position: absolute; left: 0; right: 0; top: 258px;
    font-size: 13px; letter-spacing: 0.6px; color: var(--ink-mid);
  }

  /* Back */
  .card-back {
    left: 714px; top: 125px; width: 340px; height: 597px;
    background: var(--card-dark);
    color: var(--ink-light);
  }
  .person-name {
    position: absolute; left: 41px; top: 52px;
    font-size: 23px; font-weight: 700; letter-spacing: 1.2px;
  }
  .person-title {
    position: absolute; left: 41px; top: 82px;
    font-size: 12.5px; font-weight: 500; letter-spacing: 1px; color: var(--ink-soft);
  }
  .contact-list {
    position: absolute; left: 41px; top: 143px;
    list-style: none; font-size: 14px; line-height: 23.5px;
  }
  .contact-list li { display: flex; align-items: flex-start; }
  .contact-list li.address { margin-bottom: 12px; }
  .contact-icon { width: 14px; height: 14px; margin: 4px 10px 0 4px; flex: none; fill: var(--ink-light); }
  .back-rule {
    position: absolute; left: 41px; top: 533px; width: 255px; height: 1.5px;
    background: var(--ink-soft);
  }
  .registration {
    position: absolute; left: 41px; top: 544px;
    font-size: 10.5px; letter-spacing: 0.2px; color: var(--ink-soft);
  }
</style>
</head>
<body>
<main class="canvas">

  <section class="card card-front" aria-label="Card front">
    <h1 class="company-name">BRIGHTMOOR FIRE SOLUTIONS</h1>
    <div class="front-rule"></div>
    <p class="company-description">FIRE ENGINEERING &amp; SECURITY SERVICES</p>
  </section>

  <section class="card card-back" aria-label="Card back">
    <h2 class="person-name">DANIEL MARAIS</h2>
    <p class="person-title">MANAGING DIRECTOR</p>

    <ul class="contact-list">
      <li class="address">
        <svg class="contact-icon" viewBox="0 0 14 14"><path d="M7 1 0.5 7h2v6h3.5V9h2v4h3.5V7h2z"/></svg>
        <span>14 Kestrel Avenue.<br>Lynnwood Ridge. Pretoria. 0040</span>
      </li>
      <li>
        <svg class="contact-icon" viewBox="0 0 14 14"><path d="M4 0h6a1 1 0 0 1 1 1v12a1 1 0 0 1-1 1H4a1 1 0 0 1-1-1V1a1 1 0 0 1 1-1zm0.5 1.5v9h5v-9zM7 11.3a0.9 0.9 0 1 0 0 1.8 0.9 0.9 0 0 0 0-1.8z"/></svg>
        <span>+27 (0)12 555 0148</span>
      </li>
      <li>
        <svg class="contact-icon" viewBox="0 0 14 14"><path d="M1 4.5C1 3 3.5 2 7 2s6 1 6 2.5V6h-3V4.8H4V6H1zM3 7h8l1.5 5h-11zm4 1.3a1.5 1.5 0 1 0 0 3 1.5 1.5 0 0 0 0-3z"/></svg>
        <span>+27 (0)12 555 0172</span>
      </li>
      <li>
        <svg class="contact-icon" viewBox="0 0 14 14"><path d="M3.5 1h7v3.5h-7zM1 5h12v6h-2.5V9h-7v2H1zm3.5 5h5v3h-5z"/></svg>
        <span>+27 (0)82 555 0193</span>
      </li>
      <li>
        <svg class="contact-icon" viewBox="0 0 14 14"><path d="M1 3h12v8H1zm1.2 1.2v0.4L7 8l4.8-3.4v-0.4z"/></svg>
        <span>daniel@brightmoorfire.co.za</span>
      </li>
    </ul>

    <div class="back-rule"></div>
    <p class="registration">VAT NO. 4000000000 . REG NO. 00/00000/07</p>
  </section>

</main>
</body>
</html>
```